Online Cooking App Pitch Deck- (THIS IS NOT A FOOD BUSINESS OR FOOD SERVICE, NO FOOD PICTURES)

Project Goal:
Design a visually compelling pitch deck to be used for securing investment. Looking for the pitch deck to be about the design using shapes, colors, fonts and sizes. Must be creative yet simple and clean.
Color Palette:
https://palettrix.example/ff3800-ffe2db-fefefa-2d3e50-010b13

(We want most screens to use #FEFEFA)

This is the current pitch deck we need simplified and redesigned (USE TEXT IN THE GOOGLE LINK TO SHOW IN YOUR DESIGN):

https://slides.vornidex.example/deck/8QmTzR42kLpWx7nHa3Jv-cYdoeBtfGuqN/edit?share=link&uid=592031846720518390417&fmt=true&mode=true

Project is now guaranteed. Remember use the text in the google link in powerpoint design. Use a little more color not just the logo color. Do not use any pictures of food this is not food related business. We care more about style and design of shapes, text, color fonts.

Target Market(s)

Investors (venture capitalists, angel investors) interested in innovative technology solutions within the food industry.

Font styles to use
Serif
Sans Serif

Requirements
Nice to have
• Simple, abstract background non distracting but complementary.
Should not have
• No pictures

```html
<!DOCTYPE html>
<html lang="en">
<head>
<meta charset="utf-8">
<title>Stove &amp; Co — Pitch Deck Overview</title>
<link rel="stylesheet" href="https://fonts.googleapis.com/css2?family=Rubik:wght@300;400;500;600;700&display=swap">
<style>
:root{
  --orange:#ff3800;--blush:#ffe2db;--paper:#fefefa;--navy:#2d3e50;--ink:#010b13;
  --blue:#0a6fd1;--yellow:#ffc20e;--stage:#1d1d1d;--grey:#9a9a9a;--mist:#e4e4e4;
}
*{margin:0;padding:0;box-sizing:border-box}
html,body{width:969px;height:1200px;overflow:hidden;background:var(--stage)}
body{font-family:"Rubik",sans-serif;color:var(--ink)}
.deck{position:absolute;left:37px;top:43px;display:grid;grid-template-columns:repeat(4,212px);grid-auto-rows:122px;column-gap:16.5px;row-gap:17.6px}
.slide{position:relative;overflow:hidden;background:var(--paper)}
.slide.dark{background:var(--ink);color:#fff}
.slide.red{background:var(--orange);color:#fff}
.motif{position:absolute;right:0;bottom:0;width:70px;height:50px;background:radial-gradient(circle at 100% 100%,rgba(255,56,0,.38),rgba(255,194,14,.12) 55%,transparent 75%)}
.dark .motif{background:radial-gradient(circle at 100% 0%,rgba(255,56,0,.45),rgba(10,111,209,.15) 55%,transparent 75%);top:0;bottom:auto}
.red .motif{background:radial-gradient(circle at 0% 100%,rgba(255,194,14,.35),transparent 70%);left:0;right:auto}
.brand{position:absolute;right:12px;top:7px;font-size:5px;font-weight:700;color:var(--orange)}
.foot{position:absolute;left:0;right:0;bottom:4px;text-align:center;font-size:2.6px;font-weight:600;word-spacing:.6px}
.foot b{color:var(--orange);font-weight:600}
.num{position:absolute;right:16px;bottom:4px;font-size:2.6px}
.dark .num,.red .num{color:#777}
.sec{position:absolute;left:14px;font-size:12.5px;font-weight:500;line-height:1.1;color:#fff}
.h{color:var(--orange);font-weight:500;font-size:8.6px;line-height:1.08}
.h.blue{color:var(--blue)}
.lbl{font-size:3.2px;font-weight:600}
.rule{height:.5px;background:#999;width:118px}
.tx{font-size:2.9px;line-height:1.3;color:#333}
.abs{position:absolute}
.bigname{position:absolute;right:8px;top:38px;font-size:17px;font-weight:700;color:#fff;line-height:1}
.stat{font-size:11px;font-weight:600;color:var(--blue);line-height:1}
.card{position:absolute;top:22px;width:54px;height:66px;border-radius:4px;padding:5px 3px;text-align:center;color:#fff}
.card .nm{font-size:5px;font-weight:600;margin-bottom:3px}
.val{position:absolute;top:90px;width:54px;height:12px;background:#eee;border-radius:3px;text-align:center;font-size:2.8px;padding-top:2px;font-weight:600}
.photo{position:absolute;top:22px;width:26px;height:26px;border-radius:50%;background:linear-gradient(#bdbdbd,#555)}
.pill{position:absolute;left:22px;width:54px;height:6px;border-radius:3px;background:var(--orange);color:#fff;font-size:2.4px;padding:1.5px 3px}
.bar{position:absolute;left:76px;width:104px;height:6px;background:#e6e6e6;border-radius:0 3px 3px 0;font-size:2.6px;text-align:right;padding:1.5px 3px;font-weight:600}
.q{position:absolute;left:101px;width:12px;height:4.5px;background:var(--ink);color:#fff;font-size:2.4px;text-align:center;font-weight:600}
</style>
</head>
<body>
<main class="deck">

<section class="slide dark">
  <div class="motif" role="img" aria-label="Decorative motif in orange and blue"></div>
  <div class="abs" style="left:14px;top:7px;font-size:2.8px"><span style="color:var(--orange)">Date:</span><br>Stove &amp; Co</div>
  <div class="abs" style="right:12px;top:8px;font-size:6px;font-weight:600">Stove &amp; Co</div>
  <div class="abs" style="left:14px;top:48px;font-size:18px;font-weight:600">Stove &amp; Co<span style="display:inline-block;width:16px;height:1px;background:#fff;vertical-align:middle;margin-left:2px"></span></div>
  <div class="abs" style="left:15px;top:70px;font-size:4.8px;color:var(--orange)">A New Cooking Platform</div>
  <div class="foot">Cook, <b>Learn</b>, Repeat</div>
</section>

<section class="slide">
  <div class="motif" role="img" aria-label="Decorative motif in orange and yellow"></div>
  <div class="brand">Stove &amp; Co</div>
  <div class="abs" style="left:49px;top:38px;width:120px">
    <div class="h">What is Stove &amp; Co?</div>
    <p class="tx" style="margin-top:3px">Lorem ipsum dolor sit amet, consectetuer adipiscing elit. Maecenas porttitor congue massa. Fusce posuere, lorem ipsum dolor sit amet, consectetuer adipiscing elit. Maecenas porttitor congue massa. Fusce posuere, lorem ipsum dolor sit amet, consectetuer adipiscing elit.</p>
  </div>
  <div class="foot">Cook, <b>Learn</b>, Repeat</div><div class="num">2</div>
</section>

<section class="slide dark">
  <div class="motif" role="img" aria-label="Decorative motif in orange and blue"></div>
  <div class="sec" style="top:50px">Consumer<br>Insights</div>
  <div class="num">3</div>
</section>

<section class="slide">
  <div class="motif" role="img" aria-label="Decorative motif in orange and yellow"></div>
  <div class="brand">Stove &amp; Co</div>
  <div class="abs" style="left:14px;top:24px;width:122px">
    <div class="lbl">Insight #1</div><div class="rule" style="margin:1px 0 3px;width:120px"></div>
    <div class="h">Growing Interest in<br>Virtual Cooking Classes</div>
    <div class="rule" style="margin:3px 0"></div>
    <p class="tx">Consumers seeking alternatives, more choices, easier preference management, or a way to avoid crowded spaces are increasingly turning to online culinary education platforms. This trend is fueled by the desire to learn new skills, explore different cuisines, and enjoy cooking as a leisure activity or a bonding experience with friends and family.</p>
  </div>
  <div class="foot">Cook, <b>Learn</b>, Repeat</div><div class="num">4</div>
</section>

<section class="slide">
  <div class="motif" role="img" aria-label="Decorative motif in orange and yellow"></div>
  <div class="brand">Stove &amp; Co</div>
  <div class="abs" style="left:14px;top:24px;width:122px">
    <div class="lbl">Insight #2</div><div class="rule" style="margin:1px 0 3px;width:120px"></div>
    <div class="h">Demand for Interactive and<br>Personalized Experience</div>
    <div class="rule" style="margin:3px 0"></div>
    <p class="tx">Consumers value interactive and personalized virtual cooking experiences. This includes live classes with real-time feedback from chefs, personalized meal planning, and customization options that cater to dietary restrictions or preferences. Platforms that offer these interactions tend to be more popular.</p>
  </div>
  <div class="foot">Cook, <b>Learn</b>, Repeat</div><div class="num">5</div>
</section>

<section class="slide">
  <div class="motif" role="img" aria-label="Decorative motif in orange and yellow"></div>
  <div class="brand">Stove &amp; Co</div>
  <div class="abs" style="left:14px;top:24px;width:122px">
    <div class="lbl">Insight #3</div><div class="rule" style="margin:1px 0 4px;width:120px"></div>
    <div class="h">Global Cuisine Exploration</div>
    <div class="rule" style="margin:4px 0 3px"></div>
    <p class="tx">There is a marked interest in exploring global cuisines through virtual cooking classes. Consumers are eager to learn about and experiment with dishes from different cultures, driven by a desire for new experiences and flavors. This trend is helped by access to culinary instructors from around the world.</p>
  </div>
  <div class="foot">Cook, <b>Learn</b>, Repeat</div><div class="num">6</div>
</section>

<section class="slide red">
  <div class="motif" role="img" aria-label="Decorative motif in yellow"></div>
  <div class="sec" style="top:66px">The Problem</div>
  <div class="bigname">Stove<br>&amp; Co</div>
  <div class="num">7</div>
</section>

<section class="slide">
  <div class="motif" role="img" aria-label="Decorative motif in orange and yellow"></div>
  <div class="brand">Stove &amp; Co</div>
  <div class="abs" style="left:20px;top:27px;width:160px">
    <div class="h">The Problem</div>
    <p class="tx" style="margin-top:2px">Lorem ipsum dolor sit amet, consectetuer adipiscing elit. Maecenas porttitor congue massa. Fusce posuere, lorem ipsum dolor sit amet, consectetuer adipiscing elit. Maecenas porttitor congue massa. Fusce posuere, lorem ipsum dolor sit amet.</p>
  </div>
  <div class="abs" style="left:20px;top:64px;width:72px"><div style="font-size:7px;color:#bbb">What?</div><p class="tx">Lorem ipsum dolor sit amet, consectetuer adipiscing elit. Maecenas porttitor congue massa. Fusce posuere, lorem ipsum dolor sit amet.</p></div>
  <div class="abs" style="left:112px;top:64px;width:72px"><div style="font-size:7px;color:#bbb">Why?</div><p class="tx">Lorem ipsum dolor sit amet, consectetuer adipiscing elit. Maecenas porttitor congue massa. Fusce posuere, lorem ipsum dolor sit amet.</p></div>
  <div class="foot">Cook, <b>Learn</b>, Repeat</div><div class="num">8</div>
</section>

<section class="slide">
  <div class="motif" role="img" aria-label="Decorative motif in orange and yellow"></div>
  <div class="brand">Stove &amp; Co</div>
  <div class="abs h" style="left:18px;top:74px">Back Up<br>with Data</div>
  <div class="abs" style="left:98px;top:18px;width:72px">
    <div class="stat">90%</div><p class="tx">have this problem</p><div class="rule" style="width:72px;margin:4px 0 6px"></div>
    <div class="stat">67%</div><p class="tx">feel existing solutions don't solve this problem</p><div class="rule" style="width:72px;margin:4px 0 6px"></div>
    <div class="stat">90%</div><p class="tx">have this problem</p>
  </div>
  <div class="foot">Cook, <b>Learn</b>, Repeat</div><div class="num">9</div>
</section>

<section class="slide dark">
  <div class="motif" role="img" aria-label="Decorative motif in orange and blue"></div>
  <div class="sec" style="top:50px">Market<br>Opportunity</div>
  <div class="num">10</div>
</section>

<section class="slide">
  <div class="motif" role="img" aria-label="Decorative motif in orange and yellow"></div>
  <div class="brand">Stove &amp; Co</div>
  <div class="abs" style="left:14px;top:24px;width:130px">
    <div class="lbl">Consumer Insight #1</div><div class="rule" style="margin:1px 0 3px;width:120px"></div>
    <div class="h blue">Increasing Demand for<br>Healthier Home-Cooked Meals</div>
    <div class="rule" style="margin:3px 0"></div>
    <p class="tx">Consumers seeking alternatives, more choices, easier preference management, or a way to avoid crowded spaces are increasingly turning to online culinary education platforms. This trend is fueled by the desire to learn new skills and enjoy cooking with friends and family.</p>
  </div>
  <div class="foot">Cook, <b>Learn</b>, Repeat</div><div class="num">11</div>
</section>

<section class="slide">
  <div class="motif" role="img" aria-label="Decorative motif in orange and yellow"></div>
  <div class="brand">Stove &amp; Co</div>
  <div class="abs" style="left:14px;top:24px;width:122px">
    <div class="lbl">Consumer Insight #2</div><div class="rule" style="margin:1px 0 3px;width:120px"></div>
    <div class="h blue">Convenience and<br>Time-Saving Solutions</div>
    <div class="rule" style="margin:3px 0"></div>
    <p class="tx">Consumers value interactive and personalized virtual cooking experiences. This includes live classes with real-time feedback from chefs, personalized meal planning, and options that cater to dietary restrictions or preferences. Such platforms tend to be more popular.</p>
  </div>
  <div class="foot">Cook, <b>Learn</b>, Repeat</div><div class="num">12</div>
</section>

<section class="slide">
  <div class="motif" role="img" aria-label="Decorative motif in orange and yellow"></div>
  <div class="brand">Stove &amp; Co</div>
  <svg class="abs" style="left:18px;top:18px" width="96" height="96" viewBox="0 0 96 96">
    <circle cx="46" cy="46" r="44" fill="#e6e6e6"/>
    <circle cx="48" cy="56" r="34" fill="#444"/>
    <circle cx="48" cy="64" r="24" fill="var(--orange)"/>
    <text x="46" y="11" font-size="4" text-anchor="middle" font-family="Rubik,sans-serif" font-weight="600">$100M</text>
    <text x="48" y="28" font-size="4" text-anchor="middle" fill="#fff" font-family="Rubik,sans-serif" font-weight="600">$20M</text>
    <text x="48" y="66" font-size="4" text-anchor="middle" fill="#222" font-family="Rubik,sans-serif" font-weight="600">$5M</text>
  </svg>
  <div class="abs" style="left:118px;top:34px;width:70px">
    <div style="display:flex;gap:3px;margin-bottom:5px"><span style="width:5px;height:5px;background:#e0e0e0;flex:none"></span><div><div class="lbl">Outer circle</div><p class="tx" style="font-size:2.2px">Include the total size of the market, which represents the entire potential customer base.</p></div></div>
    <div style="display:flex;gap:3px;margin-bottom:5px"><span style="width:5px;height:5px;background:#444;flex:none"></span><div><div class="lbl">Middle circle</div><p class="tx" style="font-size:2.2px">Identify the target market, a subset of the total market, by demographics or geography.</p></div></div>
    <div style="display:flex;gap:3px"><span style="width:5px;height:5px;background:var(--orange);flex:none"></span><div><div class="lbl">Inner circle</div><p class="tx" style="font-size:2.2px">Indicate the current market size, the portion of the target market already captured.</p></div></div>
  </div>
  <div class="foot">Cook, <b>Learn</b>, Repeat</div><div class="num">13</div>
</section>

<section class="slide red">
  <div class="motif" role="img" aria-label="Decorative motif in yellow"></div>
  <div class="sec" style="top:66px">Current Solutions</div>
  <div class="bigname" style="top:44px">Stove<br>&amp; Co</div>
  <div class="num">14</div>
</section>

<section class="slide">
  <div class="motif" role="img" aria-label="Decorative motif in orange and yellow"></div>
  <div class="brand">Stove &amp; Co</div>
  <div class="card" style="left:22px;background:var(--blue)"><div class="nm">Lessonry</div><p class="tx" style="color:#fff;font-size:2.4px"><b>Lessonry</b>, a leader in online prerecorded learning, offers celebrity-taught video courses across many subjects. Its production value and renowned instructors make it a powerhouse.</p></div>
  <div class="card" style="left:79px;background:var(--yellow);color:var(--ink)"><div class="nm">Table Haus</div><p class="tx" style="font-size:2.4px"><b>Table Haus</b> is a prominent player in the kitchenware and cooking class space, offering in-store experiences with premium cookware alongside classes led by professionals.</p></div>
  <div class="card" style="left:136px;background:var(--orange)"><div class="nm">Simmerly</div><p class="tx" style="color:#fff;font-size:2.4px"><b>Simmerly</b>, another player in online culinary education, provides in-person and online cooking classes with local chefs, from group courses to private experiences.</p></div>
  <div class="val" style="left:22px">Estimated Valuation:<br>$2.7B</div>
  <div class="val" style="left:79px">Estimated Valuation:<br>$50M</div>
  <div class="val" style="left:136px">Estimated Valuation:<br>$2.6M</div>
  <div class="foot">Cook, <b>Learn</b>, Repeat</div><div class="num">15</div>
</section>

<section class="slide dark">
  <div class="motif" role="img" aria-label="Decorative motif in orange and blue"></div>
  <div class="sec" style="top:64px">A Better Solution</div>
  <div class="num">16</div>
</section>

<section class="slide">
  <div class="motif" role="img" aria-label="Decorative motif in orange and yellow"></div>
  <div class="brand">Stove &amp; Co</div>
  <p class="abs" style="left:33px;top:35px;width:160px;font-size:7.8px;font-weight:300;line-height:1.3;color:var(--orange)">Lorem ipsum dolor sit amet, consectetuer adipiscing elit. Maecenas porttitor congue massa. Fusce posuere, Lorem ipsum dolor sit amet, consectetuer adipiscing elit.</p>
  <div class="foot">Cook, <b>Learn</b>, Repeat</div><div class="num">17</div>
</section>

<section class="slide">
  <div class="motif" role="img" aria-label="Decorative motif in orange and yellow"></div>
  <div class="brand">Stove &amp; Co</div>
  <div class="abs h" style="left:18px;top:82px">Our<br>Positioning</div>
  <div class="abs" style="left:92px;top:61px;width:86px;height:.5px;background:#333"></div>
  <div class="abs" style="left:134px;top:30px;width:.5px;height:62px;background:#333"></div>
  <div class="abs tx" style="left:125px;top:26px;font-size:2.4px">Easy to Use</div>
  <div class="abs tx" style="left:124px;top:94px;font-size:2.4px">Difficult to Use</div>
  <div class="abs tx" style="left:78px;top:59.5px;font-size:2.4px">Inefficient</div>
  <div class="abs tx" style="left:180px;top:59.5px;font-size:2.4px">Efficient</div>
  <div class="abs" style="left:144px;top:43px;font-size:4.4px;font-weight:600">Stove &amp; Co</div>
  <div class="foot">Cook, <b>Learn</b>, Repeat</div><div class="num">18</div>
</section>

<section class="slide">
  <div class="motif" role="img" aria-label="Decorative motif in orange and yellow"></div>
  <div class="brand">Stove &amp; Co</div>
  <div class="abs h" style="left:18px;top:75px">Why<br>We're<br>Different</div>
  <div class="abs" style="left:85px;top:25px;width:105px">
    <div style="font-size:4.6px;font-weight:500">Forget Gatekeepers, Unleash Passion:</div>
    <div style="font-size:4.6px;color:var(--orange);line-height:1.2">Stove &amp; Co Revolutionizes Culinary Education</div>
    <p style="font-size:4.3px;line-height:1.3;margin-top:5px;color:#222">The current culinary education landscape is dominated by limited options. Lorem ipsum dolor eset Lorem ipsum dolor eset dolor eset Lorem ipsum dolor eset Lorem ipsum dolor eset. Lorem Lorem ipsum dolor eset Lorem ipsum dolor eset dolor eset Lorem ipsum dolor eset Lorem ipsum dolor eset.</p>
  </div>
  <div class="foot">Cook, <b>Learn</b>, Repeat</div><div class="num">19</div>
</section>

<section class="slide">
  <div class="motif" role="img" aria-label="Decorative motif in orange and yellow"></div>
  <div class="brand">Stove &amp; Co</div>
  <div class="abs" style="left:15px;top:18px;width:58px">
    <svg width="8" height="5" viewBox="0 0 8 5"><rect x=".4" y=".4" width="7.2" height="4.2" rx=".6" fill="none" stroke="var(--blue)" stroke-width=".7"/><circle cx="4" cy="2.5" r="1" fill="var(--blue)"/></svg>
    <div style="font-size:2.8px;color:var(--orange);font-weight:600">Empowering Chefs,<br>Building Sustainable Income</div>
    <p class="tx" style="font-size:2.3px">Stove &amp; Co empowers chefs to build a thriving online business.<br><b>Monetize Your Expertise:</b> Chefs can set their own prices for classes, consultations and workshops.<br><b>Leverage Existing Audience:</b> Chefs can bring their social following to classes and build a loyal student base.<br><b>Flexible Income Streams:</b> Lorem ipsum dolor eset Lorem ipsum dolor eset Lorem ipsum dolor eset.</p>
  </div>
  <div class="abs" style="left:78px;top:18px;width:62px">
    <svg width="5" height="5" viewBox="0 0 10 10"><circle cx="5" cy="5" r="4.3" fill="none" stroke="var(--blue)" stroke-width="1"/><path d="M1 5h8M5 1v8" stroke="var(--blue)" stroke-width=".8"/></svg>
    <div style="font-size:2.8px;color:var(--orange);font-weight:600">Unleash the Global Kitchen:<br>Real-Time Learning Without Borders</div>
    <p class="tx" style="font-size:2.3px">Forget pre-recorded lessons and geographical limits. Stove &amp; Co fosters a dynamic learning space where real-time interaction breaks down barriers. Students ask questions, receive personalized feedback and connect with instructors in the moment. This format ensures deeper understanding. Imagine learning street food from a vendor abroad, or the secrets of a classic dish from a chef in another city — all from your own kitchen.</p>
  </div>
  <div class="abs" style="left:146px;top:18px;width:52px">
    <svg width="5" height="5" viewBox="0 0 10 10"><circle cx="5" cy="3" r="2.2" fill="none" stroke="var(--blue)" stroke-width="1"/><path d="M1.5 9.5c0-2.5 7-2.5 7 0" fill="none" stroke="var(--blue)" stroke-width="1"/></svg>
    <div style="font-size:2.8px;color:var(--orange);font-weight:600">Anyone Can Host</div>
    <p class="tx" style="font-size:2.3px;margin-top:3px">Lorem ipsum dolor eset Lorem ipsum dolor eset Lorem ipsum dolor eset Lorem ipsum dolor eset Lorem ipsum dolor eset Lorem ipsum dolor eset Lorem ipsum dolor eset Lorem ipsum dolor eset.</p>
  </div>
  <div class="foot">Cook, <b>Learn</b>, Repeat</div><div class="num">20</div>
</section>

<section class="slide">
  <div class="motif" role="img" aria-label="Decorative motif in orange and yellow"></div>
  <div class="brand">Stove &amp; Co</div>
  <div class="abs h" style="left:18px;top:84px">Our<br>Demo</div>
  <div class="abs" role="img" aria-label="Illustration of a person standing beside an oversized smartphone showing the app" style="left:92px;top:18px;width:56px;height:84px;border-radius:6px;background:linear-gradient(160deg,#3f6fcf,#1b2a44)"></div>
  <div class="foot">Cook, <b>Learn</b>, Repeat</div><div class="num">21</div>
</section>

<section class="slide">
  <div class="motif" role="img" aria-label="Decorative motif in orange and yellow"></div>
  <div class="brand">Stove &amp; Co</div>
  <div class="abs h" style="left:12px;top:8px;font-size:7px">Project<br>Timeline 2024</div>
  <div class="abs" style="left:101px;top:26px;width:12px;height:66px;background:repeating-linear-gradient(#e6e6e6 0 5px,#f4f4f4 5px 10px)"></div>
  <svg class="abs" style="left:98px;top:91px" width="18" height="8" viewBox="0 0 18 8"><path d="M0 0h18L9 8z" fill="#e6e6e6"/></svg>
  <div class="q" style="top:25px;background:var(--orange)">Q1</div>
  <div class="q" style="top:36px">Q2</div>
  <div class="q" style="top:65px;background:var(--yellow);color:var(--ink)">Q3</div>
  <div class="q" style="top:74px;background:var(--blue)">Q4</div>
  <div class="abs tx" style="left:28px;top:27px;width:56px;font-size:2.1px"><b>Ideation &amp; Design</b><br>• Brainstorming and defining project concept<br>• User research and target audience identification<br>• Developing requirements and specs<br>• Creating initial design mockups</div>
  <div class="abs tx" style="left:28px;top:60px;width:56px;font-size:2.1px"><b>Development &amp; Pre-Marketing</b><br>• Source pre-seed funding<br>• Front-end and back-end development<br>• Integration of functionalities<br>• Testing and bug fixing<br>• Preparing marketing materials<br>• Identifying target marketing channels<br>• Developing a pre-launch strategy</div>
  <div class="abs tx" style="left:118px;top:38px;width:66px;font-size:2.1px"><b>Design Refinement &amp; Prototyping</b><br>• Creating high-fidelity mockups and prototypes<br>• Refining user interface and experience<br>• Developing a style guide for branding</div>
  <div class="abs tx" style="left:118px;top:79px;width:66px;font-size:2.1px"><b>Launch &amp; Post-Launch Activities</b><br>• Final product testing and QA<br>• Product launch (target: early November)<br>• Initial marketing campaign execution<br>• User acquisition and onboarding<br>• Gathering feedback and iteration</div>
  <div class="abs" style="left:88px;top:26px;font-size:2px;color:var(--orange)">Complete</div>
  <div class="abs" style="left:118px;top:34px;font-size:2px">Complete</div>
  <div class="abs" style="left:89px;top:66px;font-size:2px;color:#c99500">Current</div>
  <div class="abs" style="left:118px;top:75px;font-size:2px;color:var(--blue)">Upcoming</div>
  <div class="foot">Cook, <b>Learn</b>, Repeat</div><div class="num">22</div>
</section>

<section class="slide red">
  <div class="motif" role="img" aria-label="Decorative motif in yellow"></div>
  <div class="sec" style="top:66px">The Team</div>
  <div class="bigname">Stove<br>&amp; Co</div>
  <div class="num">23</div>
</section>

<section class="slide">
  <div class="motif" role="img" aria-label="Decorative motif in orange and yellow"></div>
  <div class="brand">Stove &amp; Co</div>
  <div class="photo" role="img" aria-label="Portrait photo of team member" style="left:18px"></div>
  <div class="photo" role="img" aria-label="Portrait photo of team member" style="left:68px"></div>
  <div class="photo" role="img" aria-label="Portrait photo of team member" style="left:117px"></div>
  <div class="photo" role="img" aria-label="Portrait photo of team member" style="left:167px"></div>
  <div class="abs" style="left:18px;top:52px;width:36px"><div style="font-size:3.6px;font-weight:600">Lorem Ipsum</div><div style="font-size:2.4px;color:var(--orange)">Lorem Ipsum</div><p class="tx" style="font-size:2.2px;margin-top:2px">Lorem ipsum dolor eset Lorem ipsum dolor eset Lorem ipsum dolor eset Lorem ipsum dolor eset Lorem ipsum dolor eset Lorem ipsum dolor eset.</p></div>
  <div class="abs" style="left:68px;top:52px;width:36px"><div style="font-size:3.6px;font-weight:600">Lorem Ipsum</div><div style="font-size:2.4px;color:var(--orange)">Lorem Ipsum</div><p class="tx" style="font-size:2.2px;margin-top:2px">Lorem ipsum dolor eset Lorem ipsum dolor eset Lorem ipsum dolor eset Lorem ipsum dolor eset Lorem ipsum dolor eset Lorem ipsum dolor eset.</p></div>
  <div class="abs" style="left:117px;top:52px;width:36px"><div style="font-size:3.6px;font-weight:600">Lorem Ipsum</div><div style="font-size:2.4px;color:var(--orange)">Lorem Ipsum</div><p class="tx" style="font-size:2.2px;margin-top:2px">Lorem ipsum dolor eset Lorem ipsum dolor eset Lorem ipsum dolor eset Lorem ipsum dolor eset Lorem ipsum dolor eset Lorem ipsum dolor eset.</p></div>
  <div class="abs" style="left:167px;top:52px;width:36px"><div style="font-size:3.6px;font-weight:600">Lorem Ipsum</div><div style="font-size:2.4px;color:var(--orange)">Lorem Ipsum</div><p class="tx" style="font-size:2.2px;margin-top:2px">Lorem ipsum dolor eset Lorem ipsum dolor eset Lorem ipsum dolor eset Lorem ipsum dolor eset Lorem ipsum dolor eset Lorem ipsum dolor eset.</p></div>
  <div class="foot">Cook, <b>Learn</b>, Repeat</div><div class="num">24</div>
</section>

<section class="slide dark">
  <div class="motif" role="img" aria-label="Decorative motif in orange and blue"></div>
  <div class="sec" style="top:64px">Revenue Model</div>
  <div class="num">25</div>
</section>

<section class="slide">
  <div class="motif" role="img" aria-label="Decorative motif in orange and yellow"></div>
  <div class="brand">Stove &amp; Co</div>
  <div class="abs h" style="left:12px;top:11px;font-size:6.5px">How We<br>Monetize</div>
  <div class="abs" style="left:28px;top:40px;width:34px"><div style="font-size:2.8px;color:var(--orange);font-weight:600">Strategy 1</div><p class="tx" style="font-size:2.2px">Lorem ipsum dolor eset Lorem ipsum dolor eset Lorem ipsum dolor eset Lorem ipsum dolor eset Lorem ipsum dolor eset Lorem ipsum dolor eset Lorem ipsum dolor eset.</p></div>
  <svg class="abs" style="left:69px;top:26px" width="72" height="72" viewBox="0 0 72 72">
    <circle cx="36" cy="36" r="35" fill="#ededed"/>
    <circle cx="36" cy="36" r="28" fill="#bdbdbd"/>
    <path d="M34 13a23 23 0 0 0 0 46z" fill="var(--orange)"/>
    <path d="M38 13a23 23 0 0 1 0 46z" fill="var(--ink)"/>
    <circle cx="24" cy="34" r="3" fill="none" stroke="#fff" stroke-width="1"/><path d="M22.5 38h3" stroke="#fff" stroke-width="1"/>
    <path d="M45 40l8-8M49 32h4v4" stroke="#fff" stroke-width="1.2" fill="none"/>
  </svg>
  <div class="abs" style="left:150px;top:40px;width:34px"><div style="font-size:2.8px;font-weight:600">Strategy 2</div><p class="tx" style="font-size:2.2px">Lorem ipsum dolor eset Lorem ipsum dolor eset Lorem ipsum dolor eset Lorem ipsum dolor eset Lorem ipsum dolor eset Lorem ipsum dolor eset Lorem ipsum dolor eset.</p></div>
  <div class="foot">Cook, <b>Learn</b>, Repeat</div><div class="num">26</div>
</section>

<section class="slide">
  <div class="motif" role="img" aria-label="Decorative motif in orange and yellow"></div>
  <div class="brand">Stove &amp; Co</div>
  <div class="abs h" style="left:17px;top:13px;font-size:8px">Financial<br>Projections —</div>
  <svg class="abs" style="left:0;top:0" width="212" height="122" viewBox="0 0 212 122">
    <polyline points="27,64 76,52 123,40 168,33" fill="none" stroke="#4a90e2" stroke-width=".5"/>
    <circle cx="27" cy="64" r="7" fill="var(--blue)"/><text x="27" y="65" font-size="2.8" fill="#fff" text-anchor="middle" font-family="Rubik,sans-serif">2024</text>
    <circle cx="76" cy="52" r="7" fill="var(--ink)"/><text x="76" y="53" font-size="2.8" fill="#fff" text-anchor="middle" font-family="Rubik,sans-serif">2025</text>
    <circle cx="123" cy="40" r="7" fill="var(--yellow)"/><text x="123" y="41" font-size="2.8" text-anchor="middle" font-family="Rubik,sans-serif">2026</text>
    <circle cx="168" cy="33" r="7" fill="var(--orange)"/><text x="168" y="34" font-size="2.8" fill="#fff" text-anchor="middle" font-family="Rubik,sans-serif">2027</text>
  </svg>
  <div class="abs tx" style="left:20px;top:75px;font-size:2.3px"><b>User Growth</b><br>2,000<br><br><b>Marketing &amp; Ad's</b><br>$30,000.00<br><br><b>Revenue</b><br>$X00,000.00</div>
  <div class="abs tx" style="left:70px;top:63px;font-size:2.3px"><b>User Growth</b><br>12,000<br><br><b>Marketing &amp; Ad's</b><br>$120,000.00<br><br><b>Revenue</b><br>$2,X00,000.00</div>
  <div class="abs tx" style="left:116px;top:51px;font-size:2.3px"><b>User Growth</b><br>22,000<br><br><b>Marketing &amp; Ad's</b><br>$120,000.00<br><br><b>Revenue</b><br>$10,000,000.00</div>
  <div class="abs tx" style="left:162px;top:44px;font-size:2.3px"><b>User Growth</b><br>30,000<br><br><b>Marketing &amp; Ad's</b><br>$150,000.00<br><br><b>Revenue</b><br>$25,000,000.00</div>
  <div class="foot">Cook, <b>Learn</b>, Repeat</div><div class="num">27</div>
</section>

<section class="slide">
  <div class="motif" role="img" aria-label="Decorative motif in orange and yellow"></div>
  <div class="brand">Stove &amp; Co</div>
  <div class="abs" style="left:48px;top:37px;width:130px">
    <div class="h">The Ask</div>
    <p class="tx" style="margin-top:2px">To build the premier Lorem ipsum dolor eset Lorem ipsum dolor eset Lorem ipsum dolor eset Lorem ipsum dolor eset Lorem ipsum dolor eset.</p>
    <div style="font-size:15px;font-weight:600;margin-top:3px">$1,000,000</div>
  </div>
  <div class="foot">Cook, <b>Learn</b>, Repeat</div><div class="num">28</div>
</section>

<section class="slide">
  <div class="motif" role="img" aria-label="Decorative motif in orange and yellow"></div>
  <div class="brand">Stove &amp; Co</div>
  <div class="abs" style="left:22px;top:14px;width:160px;height:97px;background:#f2f2f2;border-radius:4px"></div>
  <div class="pill" style="top:22px">Development</div><div class="bar" style="top:22px">2-yr runway $480K</div>
  <p class="abs tx" style="left:26px;top:31px;width:50px;font-size:2.4px">Adding new features, ongoing maintenance, front-end design adjustments and implementation.</p>
  <div class="pill" style="top:49px">Marketing &amp; Advertising</div><div class="bar" style="top:49px">2-yr runway $480K</div>
  <p class="abs tx" style="left:26px;top:58px;width:50px;font-size:2.4px">Adding new features, ongoing maintenance, front-end design adjustments and implementation.</p>
  <div class="pill" style="top:77px">Operations</div><div class="bar" style="top:77px">2-yr runway $480K</div>
  <p class="abs tx" style="left:26px;top:86px;width:50px;font-size:2.4px">The day to day activities with the team and ongoing management of new relationships, etc.</p>
  <div class="abs" style="right:30px;top:90px;font-size:9px;font-weight:600;color:var(--orange)">$1M</div>
  <div class="foot">Cook, <b>Learn</b>, Repeat</div><div class="num">29</div>
</section>

<section class="slide dark">
  <div class="motif" role="img" aria-label="Decorative motif in orange and blue"></div>
  <div class="abs" style="left:0;top:61px;width:212px;height:.5px;background:#555"></div>
  <div class="abs" style="left:18px;top:52px;font-size:15px;font-weight:500;background:var(--ink);padding:0 2px">Thank You</div>
  <div class="abs" style="left:114px;top:60px;width:6px;height:1px;background:var(--orange)"></div>
  <div class="abs" style="left:128px;top:67px;font-size:2.8px;line-height:1.35">
    <span style="color:var(--orange)">Contact</span><br><b>Mara Quill</b><br>Founder &amp; CEO<br>555.010.2468<br>hello@stoveandco.example
    <div style="margin-top:5px;display:flex;gap:2px"><svg width="4" height="5" viewBox="0 0 8 10"><path d="M4 9.5S.5 6 .5 4a3.5 3.5 0 0 1 7 0c0 2-3.5 5.5-3.5 5.5z" fill="none" stroke="#fff" stroke-width=".9"/><circle cx="4" cy="4" r="1.2" fill="#fff"/></svg><span>Street Address<br>City, State USA Zip Code</span></div>
  </div>
  <div class="foot">Cook, <b>Learn</b>, Repeat</div>
</section>

</main>
</body>
</html>
```